Blow Dry Bar Business Cards

These cards must be eye catching and modern.
You must be willing to work fast and make changes.

Winner will be offered other projects

Files 1 THIS IS THE STYLE CARDS I AM INTRESTED IN!!!
Please be creative, I am paying for my own eye catching design. I need files to be prisma press ready.

COLORS THAT ARE PAINTED INSIDE MY SHOP:
- - - http://www.brenwickcoatings.example/en/explore-colors/painter/color-selector.html?colors=4007-3C

- - - http://www.tarnellhues.example/color/paint-colors/quiet-harbor-d58-2

I want the business cards sleek and modern if you use the logo please correct imperfections. I added the part that says Blow Dry Bar (see website).
Do not be afraid to separate the blow dryer from the name to make the cards look like the file with the pink elephant.

SHOULD INCLUDE
*Blow Dryer (we are a blow dry bar not a salon we do not cut or color so do not include sheers of any kind)
*BUSINESS NAME: Simply Silken Waves - Blow Dry Bar (PLEASE SEE MY WEBSITE)
* Website: SIMPLYSILKENWAVES.EXAMPLE
*Phone number (555) 014-2763
Updates

Prisma press said it can be submitted in JPG

http://www.tarnellhues.example/color/paint-colors/quiet-harbor-d58-2 http://www.brenwickcoatings.example/en/explore-colors/painter/color-selector.html?colors=4007-3C ^^^^ These links will take you to the color paint that is painted inside my shop.

Target Market(s)

AGES 18 - 55 WOMEN
HIGH END MARKET

Industry/Entity Type

Salon

Requirements
Must have
• SEE COLOR EXAMPLE FILE
BLOW DRYER
UNIQUE
I LIKE THE CARD WITH THE PINK ELEPHANT THE BEST
Nice to have
• BE AS CREATIVE AND MODERN AS POSSIBLE DO NOT COPY ANY OF THE CARDS BELOW.
Should not have
• SCISSORS
PINK

```html
<!DOCTYPE html>
<html lang="en">
<head>
<meta charset="utf-8">
<title>Simply Silken Waves – Business Cards</title>
<link rel="stylesheet" href="https://fonts.googleapis.com/css2?family=Arvo&family=Montserrat:wght@300;400&display=swap">
<style>
  :root {
    --page: #e9e6e1;
    --card-dark: #1f1f20;
    --card-mid: #2e2e30;
    --band: #f1f1f1;
    --ink-light: #f4f4f4;
    --ink-soft: #d8d8d8;
  }
  * { margin: 0; padding: 0; box-sizing: border-box; }
  html, body { width: 1200px; height: 818px; overflow: hidden; }
  body {
    background: var(--page);
    display: flex;
    align-items: center;
    justify-content: center;
    gap: 48px;
  }
  .card {
    position: relative;
    width: 540px;
    height: 309px;
    background: var(--card-dark);
    border-radius: 4px;
    overflow: hidden;
    box-shadow: 0 14px 30px rgba(0,0,0,.28);
  }
  .card-shape { position: absolute; inset: 0; width: 100%; height: 100%; }
  .brand {
    position: absolute;
    font-family: "Arvo", serif;
    color: var(--ink-light);
    font-weight: 400;
    white-space: nowrap;
  }
  .dryer-mark {
    position: absolute;
    background: var(--ink-light);
  }
  .card-front .dryer-mark {
    left: 196px;
    top: 92px;
    width: 30px;
    height: 30px;
  }
  .card-front .brand {
    left: 26px;
    top: 138px;
    font-size: 20px;
    letter-spacing: .3px;
  }
  .contact {
    position: absolute;
    left: 306px;
    top: 92px;
    list-style: none;
    font-family: "Montserrat", sans-serif;
    font-weight: 300;
    font-size: 10.5px;
    letter-spacing: .6px;
    color: var(--ink-soft);
    line-height: 2.5;
    text-transform: uppercase;
  }
  .contact .address { line-height: 1.5; margin-top: 6px; }
  .card-back .dryer-mark {
    left: 300px;
    top: 86px;
    width: 44px;
    height: 44px;
  }
  .card-back .brand {
    left: 222px;
    top: 150px;
    font-size: 24px;
  }
</style>
</head>
<body>

  <section class="card card-front" aria-label="Business card front">
    <svg class="card-shape" viewBox="0 0 540 309" preserveAspectRatio="none" aria-hidden="true">
      <defs>
        <linearGradient id="panelShade" x1="0" y1="0" x2="1" y2="1">
          <stop offset="0" stop-color="#3a3a3c"/>
          <stop offset="1" stop-color="#262628"/>
        </linearGradient>
      </defs>
      <path d="M250 0 C 270 110, 265 220, 232 309 L 540 309 L 540 0 Z" fill="var(--band)"/>
      <path d="M276 0 C 300 110, 298 220, 270 309 L 540 309 L 540 0 Z" fill="url(#panelShade)"/>
    </svg>
    <div class="dryer-mark" role="img" aria-label="Blow dryer mark"></div>
    <p class="brand">Simply Silken Waves</p>
    <ul class="contact">
      <li>(555) 014-2763</li>
      <li>SIMPLYSILKENWAVES.EXAMPLE</li>
      <li>INFO@SIMPLYSILKENWAVES.EXAMPLE</li>
      <li class="address">280 Harbor Reed Lane Suite 14<br>Marlow Springs, Texas 77000</li>
    </ul>
  </section>

  <section class="card card-back" aria-label="Business card back">
    <svg class="card-shape" viewBox="0 0 540 309" preserveAspectRatio="none" aria-hidden="true">
      <path d="M0 0 L 120 0 C 150 110, 160 220, 190 309 L 0 309 Z" fill="var(--band)"/>
      <path d="M0 0 L 94 0 C 122 110, 130 220, 156 309 L 0 309 Z" fill="var(--card-mid)"/>
    </svg>
    <div class="dryer-mark" role="img" aria-label="Blow dryer mark"></div>
    <p class="brand">Simply Silken Waves</p>
  </section>

</body>
</html>
```